Need creative website for award-winning author

I need someone to create a cool website for indie award-winning author Lorna Quibb. Right now she one young adult novel and a published short story. The site should appeal to both adults and children. The site has to needs to be available through PEXLOFT's platform.

HOME Page
About Lorna
Bio
Books
Community Projects
Appearances
Blogs & Videos
Contact
Store

Check out the following author's websites:
Mark Tilden
Sarah Kwell
Hazel Brnok
Dale Fenwright
Rick Abernath

Target Market(s)

Readers (all ages)

Industry/Entity Type

Adult

Coding

Coded - Design and coding required

Number of Pages Required

5+ page

Requirements
Must have
• Cutting edge look

```html
<!DOCTYPE html>
<html lang="en">
<head>
<meta charset="utf-8">
<title>Lorna Quibb — Award Winning Author</title>
<link href="https://fonts.googleapis.com/css2?family=Josefin+Sans:wght@300;400;600&family=Open+Sans:wght@400;600&display=swap" rel="stylesheet">
<style>
:root{
  --cyan:#1fcdf2;
  --heading:#3cb9e8;
  --nav-bg:#15261f;
  --text:#555b5f;
  --dark:#1c1c1c;
  --darker:#0f0f0f;
  --white:#ffffff;
  --gold:#e6a52a;
}
*{box-sizing:border-box;margin:0;padding:0}
html,body{width:1200px;height:3051px;overflow:hidden}
body{position:relative;font-family:"Open Sans",Arial,sans-serif;color:var(--text);background:var(--white)}
.abs{position:absolute}
h2{font-family:"Josefin Sans",Arial,sans-serif;font-weight:400;color:var(--heading)}

/* nav */
.main-nav{left:0;top:0;width:1200px;height:49px;background:var(--nav-bg);display:flex;justify-content:center;padding-left:8px}
.main-nav a{font-family:"Josefin Sans",Arial,sans-serif;font-size:16px;color:var(--white);text-decoration:none;padding:0 12px;line-height:50px}
.main-nav a.active{background:var(--cyan)}

/* hero */
.hero{left:0;top:49px;width:1200px;height:541px;background:radial-gradient(circle at 33% 35%,#f7d992 0%,#d6a457 18%,#5f8a6b 42%,#1f5a55 68%,#0f2f36 100%);overflow:hidden}
.hero-bubble{border-radius:50%;border:2px solid rgba(255,230,170,.35);background:rgba(255,225,160,.12)}
.hero-speaker{left:150px;top:20px;width:440px;height:521px;background:linear-gradient(180deg,#3a2a24 0%,#cfc8bd 40%,#8a5a33 75%,#6b4124 100%);border-radius:200px 200px 0 0;opacity:.85}
.ribbon-small{left:508px;top:191px;width:540px;height:49px;background:var(--cyan);clip-path:polygon(0 0,97% 0,100% 50%,97% 100%,3% 100%,0 50%,3% 0)}
.ribbon-small span{position:absolute;left:195px;top:8px;font-family:"Josefin Sans",Arial,sans-serif;font-size:28px;color:var(--white)}
.award-seal{left:575px;top:170px;width:86px;height:86px;border-radius:50%;background:radial-gradient(circle,#f4cf55 0%,#d69c1f 70%,#a8720f 100%)}
.ribbon-name{left:671px;top:256px;width:529px;height:81px;background:var(--cyan);clip-path:polygon(4% 0,100% 0,100% 100%,4% 100%,0 50%)}
.ribbon-name span{position:absolute;left:60px;top:12px;font-family:"Josefin Sans",Arial,sans-serif;font-size:54px;color:var(--white)}
.badges{left:651px;top:357px;display:flex;gap:12px}
.badges i{display:block;width:62px;height:62px;border-radius:50%;border:3px solid #d9d9d9}

/* about */
.about{left:0;top:590px;width:1200px;height:305px;background:linear-gradient(180deg,#ffffff 0%,#eeeeee 100%)}
.zigzag{left:0;top:880px;width:1200px;height:16px}
.about h2{left:152px;top:640px;font-size:46px}
.body-copy{font-size:13px;line-height:21px;color:var(--text)}
.about p{left:152px;top:710px;width:575px}
.btn{display:block;font-family:"Josefin Sans",Arial,sans-serif;text-align:center;border-radius:18px;color:var(--white);background:var(--cyan);font-size:16px;line-height:36px;height:36px}
.about .btn{left:152px;top:822px;width:157px}
.photo-circle{border-radius:50%;border:4px solid var(--cyan)}
.photo-large{left:846px;top:624px;width:204px;height:204px;background:linear-gradient(160deg,#eef3f6 0%,#c9d7df 50%,#7b8c97 100%)}
.photo-small{left:769px;top:718px;width:134px;height:134px;background:linear-gradient(160deg,#4a3b3a 0%,#9a7f72 50%,#2e5a86 100%)}

/* bio */
.bio h2{left:0;top:930px;width:1200px;text-align:center;font-size:46px}
.bio p{position:absolute;left:0;width:1200px;text-align:center;font-size:13.5px;color:var(--text)}

/* books */
.books{left:0;top:1212px;width:1200px;height:431px;background:radial-gradient(circle at 30% 20%,#eafaff 0%,#b9e8f3 45%,#8fd3e6 75%,#c6eef6 100%);overflow:hidden}
.books h3{position:absolute;left:152px;top:95px;font-family:"Josefin Sans",Arial,sans-serif;font-weight:400;font-size:30px;color:var(--white)}
.edition-line{position:absolute;left:152px;font-family:"Josefin Sans",Arial,sans-serif;font-size:16px;color:#222}
.edition-line b{font-weight:400;font-size:24px}
.books .btn-outline{position:absolute;left:152px;top:299px;width:163px;height:37px;border-radius:19px;background:var(--white);color:var(--cyan);font-family:"Josefin Sans",Arial,sans-serif;font-size:17px;text-align:center;line-height:38px}
.book-cover{left:824px;top:39px;width:193px;height:362px;background:linear-gradient(160deg,#5fc9ef 0%,#2a6fbf 50%,#14387a 100%);box-shadow:8px 10px 14px rgba(0,0,0,.35)}
.slider-dots{left:555px;top:397px;display:flex;gap:4px}
.slider-dots i{display:block;width:44px;height:8px;background:var(--cyan)}

/* community */
.community h2{left:152px;top:1688px;font-size:46px}
.community p{left:152px;top:1762px;width:390px}
.community .btn{left:152px;top:1932px;width:162px}
.video{left:555px;top:1692px;width:492px;height:277px;border:3px solid var(--cyan);background:linear-gradient(180deg,#b9cfe0 0%,#6f8f4e 35%,#3f6b2c 70%,#2c4d20 100%)}
.video-bar{position:absolute;left:0;bottom:0;width:100%;height:28px;background:rgba(0,0,0,.8);color:var(--white);font-size:11px;line-height:28px}

/* testimonials */
.testimonials{left:0;top:2008px;width:1200px;height:311px;background:linear-gradient(180deg,#2b2421 0%,#1c1a1a 100%)}
.testimonials h2{position:absolute;left:0;top:18px;width:1200px;text-align:center;font-size:48px;color:var(--cyan)}
.quote{position:absolute;top:105px;width:310px;text-align:center;font-size:13px;line-height:21px;color:var(--white)}
.quote.faded{color:rgba(255,255,255,.35)}
.quote .source{display:block;margin-top:10px;font-family:"Josefin Sans",Arial,sans-serif;color:var(--cyan);font-size:15px}
.quote.faded .source{color:rgba(31,205,242,.4)}
.stars{display:flex;gap:3px;justify-content:center;margin-top:4px}
.quote.faded .stars{opacity:.4}
.t-dots{position:absolute;left:575px;top:270px;display:flex;gap:6px}
.t-dots i{display:block;width:9px;height:9px;border-radius:50%;background:var(--cyan)}
.t-dots i.off{background:#9be6f7}

/* blog */
.blog h2{left:0;top:2350px;width:1200px;text-align:center;font-size:48px}
.blog-grid{left:152px;top:2427px;width:895px;height:453px;display:grid;grid-template-columns:repeat(3,1fr);grid-template-rows:repeat(2,1fr)}
.blog-img{width:100%;height:100%}
.blog-card{position:relative;background:#f3f4f5;padding:18px 10px 0 10px}
.blog-card h4{font-family:"Josefin Sans",Arial,sans-serif;font-weight:400;color:var(--heading);font-size:16px}
.blog-card time{display:block;font-size:10.5px;color:#333;margin:10px 0 6px}
.blog-card p{font-size:11.5px;line-height:17px;color:#555}
.blog-card .more{position:absolute;right:10px;bottom:4px;font-size:11px;color:var(--heading)}
.blog-card .corner{position:absolute;right:0;bottom:0;width:0;height:0;border-left:8px solid transparent;border-bottom:8px solid var(--cyan)}

/* footer */
.footer{left:0;top:2921px;width:1200px;height:96px;background:var(--dark)}
.footer h5{position:absolute;top:16px;font-family:"Josefin Sans",Arial,sans-serif;font-weight:400;font-size:20px;color:var(--white)}
.social{position:absolute;left:151px;top:50px;display:flex;gap:8px}
.social i{display:block;width:24px;height:24px;border-radius:3px}
.contact-lines{position:absolute;right:153px;top:47px;text-align:right;color:var(--white);font-size:13px;line-height:19px}
.copyright{left:0;top:3017px;width:1200px;height:34px;background:var(--darker);text-align:center;font-size:10px;line-height:34px;color:#e3c64b}
</style>
</head>
<body>

<nav class="main-nav abs">
  <a class="active">Home</a><a>About Lorna</a><a>Bio</a><a>Books</a><a>Community Projects</a><a>Appearances</a><a>Blogs &amp; Videos</a><a>Contact</a><a>Store</a>
</nav>

<header class="hero abs">
  <div class="hero-bubble abs" style="left:330px;top:10px;width:150px;height:150px"></div>
  <div class="hero-bubble abs" style="left:640px;top:40px;width:120px;height:120px"></div>
  <div class="hero-bubble abs" style="left:470px;top:130px;width:90px;height:90px"></div>
  <div class="hero-bubble abs" style="left:910px;top:30px;width:70px;height:70px"></div>
  <div class="hero-bubble abs" style="left:40px;top:300px;width:110px;height:110px"></div>
  <div class="hero-speaker abs" role="img" aria-label="Photo of the author speaking at a wooden podium with a microphone"></div>
  <div class="ribbon-small abs"><span>Award Winning Author</span></div>
  <div class="award-seal abs" role="img" aria-label="Gold award seal"></div>
  <div class="ribbon-name abs"><span>Lorna Quibb</span></div>
  <div class="badges abs" aria-label="Award badges">
    <i style="background:#8a5a3a"></i><i style="background:#9b7b3c"></i><i style="background:#e9eef5"></i><i style="background:#f1efe8"></i><i style="background:#283a86"></i><i style="background:#3f9a4d"></i>
  </div>
</header>

<section class="about">
  <div class="about abs"></div>
  <svg class="zigzag abs" viewBox="0 0 1200 16" preserveAspectRatio="none"><polygon fill="#ffffff" points="0,16 0,8 8,0 16,8 24,0 32,8 40,0 48,8 56,0 64,8 72,0 80,8 88,0 96,8 104,0 112,8 120,0 128,8 136,0 144,8 152,0 160,8 168,0 176,8 184,0 192,8 200,0 208,8 216,0 224,8 232,0 240,8 248,0 256,8 264,0 272,8 280,0 288,8 296,0 304,8 312,0 320,8 328,0 336,8 344,0 352,8 360,0 368,8 376,0 384,8 392,0 400,8 408,0 416,8 424,0 432,8 440,0 448,8 456,0 464,8 472,0 480,8 488,0 496,8 504,0 512,8 520,0 528,8 536,0 544,8 552,0 560,8 568,0 576,8 584,0 592,8 600,0 608,8 616,0 624,8 632,0 640,8 648,0 656,8 664,0 672,8 680,0 688,8 696,0 704,8 712,0 720,8 728,0 736,8 744,0 752,8 760,0 768,8 776,0 784,8 792,0 800,8 808,0 816,8 824,0 832,8 840,0 848,8 856,0 864,8 872,0 880,8 888,0 896,8 904,0 912,8 920,0 928,8 936,0 944,8 952,0 960,8 968,0 976,8 984,0 992,8 1000,0 1008,8 1016,0 1024,8 1032,0 1040,8 1048,0 1056,8 1064,0 1072,8 1080,0 1088,8 1096,0 1104,8 1112,0 1120,8 1128,0 1136,8 1144,0 1152,8 1160,0 1168,8 1176,0 1184,8 1192,0 1200,8 1200,16"/></svg>
  <h2 class="abs">About Lorna</h2>
  <p class="abs body-copy">Lorem Ipsum is simply dummy text of the printing and typesetting industry. Lorem Ipsum has been the industry's standard dummy text ever since the 1500s, when an unknown printer took a galley of type and scrambled it to make a type specimen book. It has survived not only five centuries, but also the leap into electronic typesetting, remaining essentially unchanged.</p>
  <a class="btn abs">Read More</a>
  <div class="photo-circle photo-large abs" role="img" aria-label="Photo of the author holding her award certificate"></div>
  <div class="photo-circle photo-small abs" role="img" aria-label="Portrait photo of the author"></div>
</section>

<section class="bio">
  <h2 class="abs">Author Bio</h2>
  <p style="top:998px">Lorna Quibb spent most of her adult life working on projects that empower youth to achieve their dreams.</p>
  <p style="top:1039px">Paper Kites, inspired by volunteerism on her daughter's neighborhood swim&nbsp; team, is a creative extension of her work as a</p>
  <p style="top:1065px">community planner.</p>
  <p style="top:1099px">She currently lives with her husband, two daughters and three dogs in Valencia, California, where she co</p>
  <p style="top:1136px">owns a</p>
  <p style="top:1158px">community planning firm.</p>
</section>

<section class="books abs">
  <h3>Edition</h3>
  <div class="edition-line" style="top:150px">Hardcover, <b>294 pages, $26.99</b> (Retail up to 55% discount and returnable)</div>
  <div class="edition-line" style="top:199px">Softcover, <b>294 pages, $15.99</b> (Retail up to 55% discount and returnable)</div>
  <div class="edition-line" style="top:242px">E-book, <b>294 pages, $4.99</b></div>
  <a class="btn-outline">Buy Online Now</a>
  <div class="book-cover abs" role="img" aria-label="Cover of the novel Paper Kites with a hummingbird illustration"></div>
  <div class="slider-dots abs"><i></i><i></i></div>
</section>

<section class="community">
  <h2 class="abs">Community Projects</h2>
  <p class="abs body-copy">Lorem Ipsum is simply dummy text of the printing and typesetting industry. Lorem Ipsum has been the industry's standard dummy text ever since the 1500s, when an unknown printer took a galley of type and scrambled it to make a type specimen book. It has survived not only five centuries, but also the leap into electronic typesetting, remaining essentially unchanged. It was popularised in the 1960s with the release of Letraset sheets containing Lorem</p>
  <a class="btn abs">Read More</a>
  <div class="video abs" role="img" aria-label="Video of volunteers working in a community garden">
    <div class="video-bar">
      <svg width="120" height="28" viewBox="0 0 120 28" style="position:absolute;left:8px;top:0"><polygon points="4,9 4,19 12,14" fill="#fff"/><polygon points="22,9 22,19 28,14" fill="#fff"/><rect x="29" y="9" width="2" height="10" fill="#fff"/><polygon points="40,12 44,12 48,8 48,20 44,16 40,16" fill="#fff"/><text x="58" y="18" fill="#fff" font-size="11" font-family="Open Sans,Arial,sans-serif">0:09 / 5:37</text></svg>
      <svg width="110" height="28" viewBox="0 0 110 28" style="position:absolute;right:6px;top:0"><rect x="4" y="9" width="16" height="11" rx="2" fill="#fff"/><circle cx="38" cy="14" r="6" fill="none" stroke="#fff" stroke-width="3"/><rect x="56" y="9" width="18" height="11" fill="none" stroke="#fff" stroke-width="2"/><path d="M88 8h5M88 8v5M104 8h-5M104 8v5M88 20h5M88 20v-5M104 20h-5M104 20v-5" stroke="#fff" stroke-width="2"/></svg>
    </div>
  </div>
</section>

<section class="testimonials abs">
  <h2>What Our Client Says</h2>
  <div class="quote faded" style="left:99px">"An entertaining story... Her characters are well-drawn and diverse and her portrait of Summer's Japanese-American grandmother is particularly charming."<span class="source">Kestrel Reviews</span>
    <div class="stars"><svg width="92" height="16" viewBox="0 0 92 16"><g fill="#e6a52a"><polygon points="8,0 10,6 16,6 11,10 13,16 8,12 3,16 5,10 0,6 6,6"/><polygon transform="translate(19 0)" points="8,0 10,6 16,6 11,10 13,16 8,12 3,16 5,10 0,6 6,6"/><polygon transform="translate(38 0)" points="8,0 10,6 16,6 11,10 13,16 8,12 3,16 5,10 0,6 6,6"/><polygon transform="translate(57 0)" points="8,0 10,6 16,6 11,10 13,16 8,12 3,16 5,10 0,6 6,6"/><polygon transform="translate(76 0)" points="8,0 10,6 16,6 11,10 13,16 8,12 3,16 5,10 0,6 6,6"/></g></svg></div>
  </div>
  <div class="quote" style="left:432px;width:336px">"A powerful story with a uniquely contemporary heroine and timeless themes of love, family, friendships, andself-acceptance."<br>—<span class="source" style="margin-top:2px">Forepage Reviews</span>
    <div class="stars"><svg width="92" height="16" viewBox="0 0 92 16"><g fill="#e6a52a"><polygon points="8,0 10,6 16,6 11,10 13,16 8,12 3,16 5,10 0,6 6,6"/><polygon transform="translate(19 0)" points="8,0 10,6 16,6 11,10 13,16 8,12 3,16 5,10 0,6 6,6"/><polygon transform="translate(38 0)" points="8,0 10,6 16,6 11,10 13,16 8,12 3,16 5,10 0,6 6,6"/><polygon transform="translate(57 0)" points="8,0 10,6 16,6 11,10 13,16 8,12 3,16 5,10 0,6 6,6"/><polygon transform="translate(76 0)" points="8,0 10,6 16,6 11,10 13,16 8,12 3,16 5,10 0,6 6,6"/></g></svg></div>
  </div>
  <div class="quote faded" style="left:790px">"An entertaining story... Her characters are well-drawn and diverse and her portrait of Summer's Japanese-American grandmother is particularly charming."<span class="source">Kestrel Reviews</span>
    <div class="stars"><svg width="92" height="16" viewBox="0 0 92 16"><g fill="#e6a52a"><polygon points="8,0 10,6 16,6 11,10 13,16 8,12 3,16 5,10 0,6 6,6"/><polygon transform="translate(19 0)" points="8,0 10,6 16,6 11,10 13,16 8,12 3,16 5,10 0,6 6,6"/><polygon transform="translate(38 0)" points="8,0 10,6 16,6 11,10 13,16 8,12 3,16 5,10 0,6 6,6"/><polygon transform="translate(57 0)" points="8,0 10,6 16,6 11,10 13,16 8,12 3,16 5,10 0,6 6,6"/><polygon transform="translate(76 0)" points="8,0 10,6 16,6 11,10 13,16 8,12 3,16 5,10 0,6 6,6"/></g></svg></div>
  </div>
  <div class="t-dots"><i class="off"></i><i></i><i></i><i></i></div>
</section>

<section class="blog">
  <h2 class="abs">Our Blog</h2>
  <div class="blog-grid abs">
    <div class="blog-img" role="img" aria-label="Photo of two children sitting on grass in a park" style="background:linear-gradient(180deg,#cfe89a 0%,#8fc04a 55%,#5e9a2c 100%)"></div>
    <article class="blog-card"><h4>Typesetting Industry</h4><time>31 March 2017</time><p>Lorem Ipsum is simply dummy text of the printing and typesetting industry. Lorem Ipsum has been the industry's standard dummy text ever since the 1500s, when an unknown printer took a galley of type and scrambled it to make a type specimen book. It has survived</p><span class="more">Read More</span><span class="corner"></span></article>
    <div class="blog-img" role="img" aria-label="Photo of a mother and daughter among purple flowers" style="background:linear-gradient(160deg,#f3c6d9 0%,#b06ad0 50%,#6b3aa0 100%)"></div>
    <article class="blog-card"><h4>Typesetting Industry</h4><time>31 March 2017</time><p>Lorem Ipsum is simply dummy text of the printing and typesetting industry. Lorem Ipsum has been the industry's standard dummy text ever since the 1500s, when an unknown printer took a galley of type and scrambled it to make a type specimen book. It has survived</p><span class="more">Read More</span><span class="corner"></span></article>
    <div class="blog-img" role="img" aria-label="Photo of children jumping outdoors under a blue sky" style="background:linear-gradient(180deg,#8fc6ea 0%,#c9e2f2 55%,#9fb86a 100%)"></div>
    <article class="blog-card"><h4>Typesetting Industry</h4><time>31 March 2017</time><p>Lorem Ipsum is simply dummy text of the printing and typesetting industry. Lorem Ipsum has been the industry's standard dummy text ever since the 1500s, when an unknown printer took a galley of type and scrambled it to make a type specimen book. It has survived</p><span class="more">Read More</span><span class="corner"></span></article>
  </div>
</section>

<footer class="footer abs">
  <h5 style="left:151px">Follow Us</h5>
  <div class="social" aria-label="Social media links">
    <i style="background:#3b67c4" aria-label="Friendspace"></i><i style="background:#2aa9e0" aria-label="Chirpline"></i><i style="background:#d9473a" aria-label="Circleup"></i><i style="background:#d8322a" aria-label="Clipcast"></i><i style="background:#e2563b" aria-label="Snapgrid"></i>
  </div>
  <h5 style="right:153px">Contact Us</h5>
  <div class="contact-lines">hello@quibbbooks.net<br>0800-555-014-2290</div>
</footer>
<div class="copyright abs">© 2017 Lorna Quibb</div>

</body>
</html>
```